わたしたち 株式会社青葉堂は、千葉県君津市で《はちみつを五感で楽しむ》をコンセプトとした 「りんごとシードルの青葉堂」という観光施設を運営している会社です。 観光バスツアーの立ち寄りスポットとしてもご愛顧いただき、年間約30万人のお客さまにお越しいただいております。 今回募集をするのは、店舗で新発売をする「はちみつレモンリキュール(仮)」のパッケージデザインです。 ------------------------ ■提案物 :新商品のパッケージデザイン ■商品 :はちみつレモンリキュール(仮) デザインと併せて商品名もご提案いただけると幸いです。 ■サイズ・販売価格 :500ml ¥1580 :375ml ¥1280 :300ml ¥1180 ※瓶によって金額が変わりますが、上記はあくまでも予定です。 ■ターゲット :20代~30代 どちらかというと女性が手に取りやすいイメージ ■コンセプト :この度の新商品は当社でこれまで販売してきた発酵により製造される各種ミードとは異なり、 梅酒のように果実・果皮をお酒に漬け、味や香りを抽出したのものをベースとしております。 本商品は、リキュール初商品のため皆様にも馴染みのある「はちみつレモン味」を採用し、 これを足掛かりに今後もリキュールの商品を展開していこうと考えております。 蜂蜜の甘さだけでなく、レモンの酸味や香りにこだわり、甘味と酸味のバランスをとることで どなたでも美味しく召し上がっていただける味を目指しました。 ■デザインイメージ :自社で販売している「ミード(蜂蜜酒)」とは全く異なるイラストや構成でお願いいたします。 今後、異なる味のリキュールを出した際にも使用できるような汎用性のあるデザイン且つ、 一目で何味かが分かるようなイラストやデザイン、構成でお願いいたします。 本商品は希釈して飲むものとなっている為、正面から見える位置に希釈して飲む商品だと分かる ようにデザインもしくは文字をいれて下さい。(3倍希釈) ■味の特徴 :レモン果汁を使用することにより、蜂蜜の甘さの中に爽やかなレモンの味わいや香りが感じられます。 蜂蜜は全体の4分の1を使用しており、その全てが純粋蜂蜜(国産と海外産を併用)となっております。 レモン果皮を漬けたお酒を用いたため、レモンの香りが強く感じられます。 その後から蜂蜜の甘い香りが鼻からぬけていきます。 【希釈前 アルコール度数 12% 糖度 約35度】 ■他社との違い :蜂蜜の内約50%は国産蜂蜜(国産蜂蜜は百花蜂蜜、その他はオレンジ蜂蜜を予定。割合は検討中)を使用する事を検討しています。 レモン果皮を用いることでレモンの香りを強く出しております。 レモン果汁はレモンの風味が強く感じられるものを採用いたしました。 はちみつ屋が作ったリキュール ■見た目の特徴 :色は黄金色で、瓶底に白色のレモン果汁やレモン果皮の成分が沈殿しております。 【応募方法】 ➀自分のイメージに合う瓶をお選び下さい。※添付資料参考 (瓶によってラベルの形及び大きさが違います) ➁透明瓶・フロスト瓶(すりガラス瓶)をお選びください。 (どちらでも良い場合はその旨ご記載ください) ③瓶の種類が決定したら、それぞれの瓶に対応したラベルの形・大きさでデザインをお願いいたします。※添付資料参考 ④選んだ瓶の番号及び瓶の種類を記載してご応募ください。 (応募記入例) ➀500ml四角瓶(縦長) フロスト瓶 ➁デザイン添付 |
この度も誠に多くのクリエイター様にご応募いただきまして、
心より感謝申し上げます。
本当にいつもクオリティの高いデザインで、
社内でもかなり悩みました。
クオリティの高いデザインの中でも、今回採用させていただいたデザインはとても目を惹き、
弊社商品の中でも今までなかったデザイン性が決めてとなりました。
多くの商品が新商品としてでておりましたが、
今回はリキュールという初めての商品で
今までにないデザインをという弊社の想いが
このデザインで表現されていると感じたので採用いたしました。
いつも本当に多くのクリエイターの皆様にお力添えをいただき
大変感謝しております。
誠にありがとうございます。
この度も非常にデザイン性の高いものばかりで
決定までにお時間を頂戴しました。
クリエイターの皆様のお力があってこその新商品でございます。
また、これからも新商品が出る際にはこちらで募集をかけさせていただきたいと考えております。
その際は、また是非お力添えをいただけますと幸いでございます。
本当に多くの方のご参加そしてご応募、
誠にありがとうございました。

```html
<!DOCTYPE html>
<html lang="ja">
<head>
<meta charset="utf-8">
<title>はちみつレモンリキュール ラベルデザイン</title>
<link rel="stylesheet" href="https://fonts.googleapis.com/css2?family=Noto+Serif+JP:wght@400;600&family=Noto+Sans+JP:wght@500&display=swap">
<style>
  :root {
    --page: #ffffff;
    --ink: #1a1a1a;
    --label-top: #fbfbfb;
    --label-bottom: #eceef0;
    --label-edge: #9a9a9a;
    --mark: #3a3a3a;
    --lemon-light: #f6dc4a;
    --lemon-deep: #e9b814;
    --leaf: #4f8a2e;
    --amber-light: #f3a21c;
    --amber-mid: #e88a0c;
    --amber-deep: #c96a06;
    --cap: #111111;
  }
  html, body {
    margin: 0;
    padding: 0;
    overflow: hidden;
  }
  body {
    width: 1200px;
    height: 900px;
    background: var(--page);
    position: relative;
    font-family: "Noto Serif JP", serif;
    color: var(--ink);
  }
  .bottle-spec {
    position: absolute;
    top: 22px;
    left: 995px;
    font-family: "Noto Sans JP", sans-serif;
    font-weight: 500;
    font-size: 21px;
    line-height: 50px;
    white-space: nowrap;
  }
  .label {
    position: absolute;
    left: 234px;
    top: 246px;
    width: 330px;
    height: 636px;
    box-sizing: border-box;
    border: 2px solid var(--label-edge);
    background: linear-gradient(160deg, var(--label-top), var(--label-bottom));
    overflow: hidden;
  }
  .label__title {
    position: absolute;
    writing-mode: vertical-rl;
    font-weight: 600;
    font-size: 52px;
    line-height: 56px;
    width: 56px;
    letter-spacing: 7px;
    margin: 0;
    white-space: nowrap;
  }
  .label__title--main { left: 78px; top: 8px; }
  .label__title--sub { left: 8px; top: 68px; }
  .label__mark {
    position: absolute;
    left: 198px;
    top: 128px;
    width: 48px;
    height: 48px;
    border-radius: 50%;
    background: var(--mark);
  }
  .label__specs {
    position: absolute;
    left: 190px;
    top: 238px;
    font-size: 13px;
    line-height: 17px;
    white-space: nowrap;
  }
  .label__honey {
    position: absolute;
    left: 190px;
    top: 290px;
    font-size: 19px;
    line-height: 26px;
    white-space: nowrap;
  }
  .label__lemons {
    position: absolute;
    left: 36px;
    top: 432px;
    width: 196px;
    height: 112px;
    border-radius: 50px 50px 40px 40px;
    background: radial-gradient(circle at 50% 55%, var(--lemon-light), var(--lemon-deep) 65%, var(--leaf));
  }
  .label__bee {
    position: absolute;
    left: 232px;
    top: 428px;
    width: 54px;
    height: 54px;
    border-radius: 50%;
    background: var(--mark);
  }
  .label__dilution, .label__volume {
    position: absolute;
    left: 0;
    width: 100%;
    text-align: center;
    font-size: 15px;
    line-height: 20px;
  }
  .label__dilution { top: 566px; }
  .label__volume { top: 598px; }
  .bottle {
    position: absolute;
    left: 570px;
    top: 0;
  }
</style>
</head>
<body>
  <div class="bottle-spec">
    <div>ボトル：No_①</div>
    <div>フロストタイプ</div>
  </div>

  <section class="label">
    <h1 class="label__title label__title--main">はちみつレモン</h1>
    <p class="label__title label__title--sub">リキュール</p>
    <div class="label__mark"></div>
    <div class="label__specs">希釈前<br>アルコール度数 12%<br>糖度 約35度</div>
    <div class="label__honey">国産蜂蜜 50%</div>
    <div class="label__lemons" role="img" aria-label="葉のついたレモンのイラスト"></div>
    <div class="label__bee"></div>
    <div class="label__dilution">3倍希釈</div>
    <div class="label__volume">300ml ¥1180</div>
  </section>

  <svg class="bottle" width="430" height="900" viewBox="0 0 430 900" role="img" aria-label="黄金色のリキュールが入ったフロスト瓶">
    <defs>
      <linearGradient id="liquid" x1="0" x2="1" y1="0" y2="0">
        <stop offset="0" stop-color="var(--amber-deep)"/>
        <stop offset="0.3" stop-color="var(--amber-light)"/>
        <stop offset="0.7" stop-color="var(--amber-mid)"/>
        <stop offset="1" stop-color="var(--amber-deep)"/>
      </linearGradient>
    </defs>
    <path d="M128 88 H230 V150 Q230 175 262 185 Q395 200 398 250 V860 Q398 886 372 886 H38 Q12 886 12 860 V250 Q15 200 150 185 Q128 175 128 150 Z" fill="url(#liquid)"/>
    <rect x="120" y="12" width="120" height="82" rx="8" fill="var(--cap)"/>
  </svg>
</body>
</html>
```